Scrapbooking company needs to design wordpress

We need a wordpress design. We are a workshop scrap products, we make products and courses. We would like something to convey the idea of ​​creativity, colors, paintings, clippings ...

Font styles to use
Decorative
Script

```html
<!DOCTYPE html>
<html lang="en">
<head>
<meta charset="utf-8">
<title>Crafthouse Studio – Blog</title>
<link rel="stylesheet" href="https://fonts.googleapis.com/css2?family=Roboto:wght@300;400;500;700&family=Roboto+Condensed:wght@400;700&family=Lobster&display=swap">
<style>
:root{
  --red:#f0494c;
  --red-dark:#d63a3d;
  --teal:#1fb5b0;
  --yellow:#f0c43f;
  --ink:#333;
  --muted:#8a8a8a;
  --line:#e4e4e4;
  --paper:#fff;
  --hero-pink:#d9446d;
  --avatar:#e3e3e3;
}
*{box-sizing:border-box;margin:0;padding:0}
html,body{width:1200px;height:3191px;overflow:hidden;background:var(--paper)}
body{position:relative;font-family:"Roboto",Arial,sans-serif;color:var(--ink);font-size:11px}
a{color:inherit;text-decoration:none}

/* top bar */
.topbar{position:absolute;left:0;top:0;width:1200px;height:68px;border-top:4px solid var(--teal)}
.follow{position:absolute;left:132px;top:18px;display:flex;align-items:center;gap:6px;font-size:10px;color:var(--muted)}
.follow .dot{width:26px;height:26px;border-radius:50%;display:inline-block}
.dot.a{background:#3b5a9a}.dot.b{background:#2aa9e0}.dot.c{background:#d8322b}.dot.d{background:#a7795b}
.search{position:absolute;left:860px;top:16px;width:204px;height:32px;border:1px solid #ccc;border-radius:16px;padding:0 16px;display:flex;align-items:center;justify-content:space-between;font-size:10px;color:#999}

/* nav */
.nav{position:absolute;left:136px;top:68px;width:950px;height:48px;background:var(--red);display:flex;justify-content:space-around;align-items:center;z-index:3}
.nav::before,.nav::after{content:"";position:absolute;top:0;border-top:48px solid var(--red-dark)}
.nav::before{left:-14px;border-left:14px solid transparent}
.nav::after{right:-14px;border-right:14px solid transparent}
.nav a{color:#fff;font-family:"Roboto Condensed",Arial,sans-serif;font-size:12px;text-transform:uppercase}

/* hero */
.hero{position:absolute;left:0;top:90px;width:1200px;height:512px;background:linear-gradient(90deg,#d9cfd6 0%,#ece8e6 40%,#f1eeea 100%)}
.hero-art{position:absolute;left:0;top:0;width:620px;height:512px;background:radial-gradient(circle at 40% 50%,#f7f3f1 0%,#e3cfd7 45%,#cbb7c4 100%)}
.hero-title{position:absolute;left:630px;top:204px;font-family:"Lobster",cursive;font-weight:400;font-size:54px;color:var(--hero-pink)}
.hero-text{position:absolute;left:660px;top:288px;width:410px;text-align:right;font-size:12.5px;line-height:28px;color:#444}
.btn{position:absolute;top:386px;height:36px;border-radius:18px;color:#fff;font-size:11px;display:flex;align-items:center;justify-content:center}
.btn.view{left:845px;width:106px;background:var(--red)}
.btn.start{left:960px;width:106px;background:var(--teal)}
.hero-dots{position:absolute;left:1024px;top:462px;display:flex;gap:6px}
.hero-dots i{width:14px;height:14px;border:2px solid #fff;border-radius:50%}

/* headings */
.sec-title{position:absolute;font-family:"Roboto Condensed",Arial,sans-serif;font-weight:400;text-transform:uppercase;color:var(--ink)}
.sec-title::after{content:"";position:absolute;left:0;bottom:-8px;width:64px;height:2px;background:var(--teal)}
.blog-title{left:130px;top:648px;font-size:22px}
.side-title{font-size:14px}

/* post cards */
.card{position:absolute;border:1px solid var(--line);background:#fff}
.photo{position:absolute;border:8px solid #fff;box-shadow:0 0 0 1px #ddd}
.photo::before,.photo::after{content:"";position:absolute;inset:-14px;border:1px solid #ddd;z-index:-1}
.photo::before{transform:rotate(-4deg)}
.photo::after{transform:rotate(3deg)}
.photo .pin{position:absolute;left:50%;top:-20px;width:16px;height:16px;border-radius:50%;background:#d61f4e;margin-left:-8px}
.photo .pin::after{content:"";position:absolute;left:7px;top:14px;width:2px;height:10px;background:#999}
.fill{width:100%;height:100%}
.post-head{display:flex;align-items:flex-start;gap:8px}
.num{flex:none;width:26px;height:26px;border-radius:50%;background:var(--teal);color:#fff;font-size:11px;display:flex;align-items:center;justify-content:center}
.post-title{font-family:"Roboto Condensed",Arial,sans-serif;font-weight:400;font-size:15px;line-height:24px;color:#333}
.excerpt{font-size:10.5px;line-height:20px;color:var(--muted)}
.posted{font-size:10px;color:var(--muted)}
.meta{display:flex;gap:22px;font-size:10px;color:var(--muted);border-top:1px solid var(--line);padding-top:14px}
.meta span::before{content:"";display:inline-block;width:8px;height:8px;background:#999;border-radius:50%;margin-right:6px;vertical-align:middle}
.body-wide{position:absolute;left:400px;width:246px}
.body-sm{position:absolute;left:22px;right:22px}

/* sidebar */
.side-box{position:absolute;left:819px;width:249px;border:1px solid var(--line)}
.pop{display:flex;gap:14px;padding:14px;border-bottom:1px solid #f0f0f0;height:96px}
.pop .th{width:85px;height:64px;flex:none}
.pop p{font-size:10px;line-height:18px;color:#555}
.pop .date{color:var(--red)}
.cat{height:40px;display:flex;align-items:center;padding:0 12px;font-size:10.5px;color:#777;border-bottom:1px solid #f2f2f2}
.cat .ic{width:16px;height:16px;border:1px solid #bbb;border-radius:50%;margin-right:20px;flex:none}
.cat .count{margin-left:auto}
.tweet{height:153px;padding:16px 14px;border-bottom:1px solid #eee}
.tweet .av{display:block;width:64px;height:48px;background:var(--avatar);margin:0 0 10px 24px}
.tweet .row{display:flex;gap:8px}
.tweet .bird{width:14px;height:12px;background:#2aa9e0;border-radius:6px;margin-top:6px;flex:none}
.tweet p{font-size:10px;line-height:20px;color:#666;font-style:italic}
.tweet b{color:var(--teal);font-weight:400}
.tweet .ago{color:var(--teal)}

/* red band */
.band{position:absolute;left:0;top:2319px;width:1200px;height:484px;background:var(--red)}
.mini{position:absolute;top:56px;width:224px;height:372px;background:#fff}
.mini .photo{left:24px;top:28px;width:176px;height:120px;border-width:6px}
.mini .photo::before,.mini .photo::after{inset:-8px}
.mini .body{position:absolute;left:18px;right:14px;top:190px}
.mini .post-title{font-size:12.5px}
.mini .num{width:24px;height:24px}
.mini .meta{gap:18px;padding-top:10px}

/* newsletter */
.news{position:absolute;left:0;top:2803px;width:1200px;height:93px;background:var(--teal)}
.news .env{position:absolute;left:132px;top:14px}
.news h3{position:absolute;left:240px;top:30px;color:#fff;font-family:"Roboto Condensed",Arial,sans-serif;font-weight:400;font-size:24px}
.news .field{position:absolute;left:530px;top:26px;width:406px;height:40px;background:#fff;border-radius:20px;padding-left:18px;display:flex;align-items:center;font-size:10px;color:#777}
.news .go{position:absolute;left:945px;top:26px;width:120px;height:40px;background:var(--yellow);border-radius:20px;color:#fff;font-size:11px;display:flex;align-items:center;justify-content:center}

/* footer */
.footer{position:absolute;left:0;top:2896px;width:1200px;height:228px;border-bottom:1px solid var(--line)}
.brand{position:absolute;left:132px;top:66px;font-family:"Roboto Condensed",Arial,sans-serif;font-weight:400;font-size:19px;color:var(--red)}
.about{position:absolute;left:132px;top:150px;width:240px;font-size:10px;line-height:18px;color:#666}
.about a{color:var(--red);text-decoration:underline}
.fcol{position:absolute;top:40px}
.fcol h4{font-family:"Roboto Condensed",Arial,sans-serif;font-weight:400;font-size:12px;text-transform:uppercase;margin-bottom:16px}
.fcol li{list-style:none;font-size:10px;line-height:20px;color:#666}
.fcol li::before{content:"› ";color:#999}
.contact li{display:flex;gap:10px;line-height:26px}
.contact li::before{content:"";width:12px;height:12px;background:var(--teal);border-radius:2px;margin-top:7px;flex:none}
.copy{position:absolute;left:0;top:3124px;width:1200px;height:67px;display:flex;align-items:center;justify-content:center;font-size:10px;color:#777}
.copy .ver{position:absolute;right:130px}
</style>
</head>
<body>

<header class="topbar">
  <div class="follow">Follow Us <i class="dot a"></i><i class="dot b"></i><i class="dot c"></i><i class="dot d"></i></div>
  <div class="search">Search
    <svg width="11" height="11" viewBox="0 0 12 12"><circle cx="5" cy="5" r="4" fill="none" stroke="#2a9a6a" stroke-width="1.6"/><line x1="8" y1="8" x2="11" y2="11" stroke="#2a9a6a" stroke-width="1.6"/></svg>
  </div>
</header>

<nav class="nav">
  <a>Home</a><a>About Us</a><a>Services</a><a>Products</a><a>Courses</a><a>Blog</a><a>Contact Us</a>
</nav>

<section class="hero">
  <div class="hero-art" role="img" aria-label="Craft table with hands drawing on a card surrounded by paper flowers, ribbons and punches"></div>
  <h1 class="hero-title">Scrapbooking Jobs</h1>
  <p class="hero-text">Nemo enim ipsam voluptatem quia voluptas sit aspernatur aut odit aut fugit, sed quia consequuntur magni dolores ratione...</p>
  <a class="btn view">View More Info</a>
  <a class="btn start">Get Start Today</a>
  <div class="hero-dots"><i></i><i></i></div>
</section>

<h2 class="sec-title blog-title">Blog</h2>

<article class="card" style="left:130px;top:702px;width:666px;height:315px">
  <div class="photo" style="left:53px;top:47px;width:292px;height:215px"><span class="pin"></span><div class="fill" role="img" aria-label="Hands cutting coloured paper shapes" style="background:linear-gradient(135deg,#e86a8a,#f2b8c6)"></div></div>
  <div class="body-wide" style="left:404px;top:56px">
    <div class="post-head"><span class="num">01</span><h3 class="post-title">Numquam eius modi tempora dolore magnam aliquam...</h3></div>
    <p class="excerpt" style="margin-top:12px">Numquam eius modi tempora dunt magna aliq uam quaerat voluptatem. Ut enim minima veniam, quis nostrum exercit...</p>
    <p class="posted" style="margin-top:14px">Posted on 23 March,2017</p>
    <div class="meta" style="margin-top:14px"><span>12 Likes</span><span>32 Comments</span><span>Share</span></div>
  </div>
</article>

<article class="card" style="left:130px;top:1036px;width:323px;height:443px">
  <div class="photo" style="left:44px;top:48px;width:237px;height:170px"><span class="pin"></span><div class="fill" role="img" aria-label="Paper hearts on a wooden table" style="background:linear-gradient(135deg,#7a4630,#c98c72)"></div></div>
  <div class="body-sm" style="top:262px">
    <div class="post-head"><span class="num">02</span><h3 class="post-title">Numquam eius modi tempora</h3></div>
    <p class="excerpt" style="margin-top:8px">Numquam eius modi tempora dunt magna aliq uam veniam, quis nostrum exercit...</p>
    <p class="posted" style="margin-top:12px">Posted on 23 March,2017</p>
    <div class="meta" style="margin-top:14px"><span>12 Likes</span><span>32 Comments</span><span>Share</span></div>
  </div>
</article>

<article class="card" style="left:472px;top:1036px;width:324px;height:443px">
  <div class="photo" style="left:44px;top:48px;width:237px;height:170px"><span class="pin"></span><div class="fill" role="img" aria-label="Blue patterned handmade card" style="background:linear-gradient(135deg,#1d3f86,#6f8fd1)"></div></div>
  <div class="body-sm" style="top:262px">
    <div class="post-head"><span class="num">03</span><h3 class="post-title">Numquam eius modi tempora</h3></div>
    <p class="excerpt" style="margin-top:8px">Numquam eius modi tempora dunt magna aliq uam veniam, quis nostrum exercit...</p>
    <p class="posted" style="margin-top:12px">Posted on 23 March,2017</p>
    <div class="meta" style="margin-top:14px"><span>12 Likes</span><span>32 Comments</span><span>Share</span></div>
  </div>
</article>

<article class="card" style="left:130px;top:1500px;width:666px;height:315px">
  <div class="photo" style="left:53px;top:47px;width:292px;height:215px"><span class="pin"></span><div class="fill" role="img" aria-label="Red scrapbook album with stamped cover" style="background:linear-gradient(135deg,#b3132a,#e8a0a6)"></div></div>
  <div class="body-wide" style="left:404px;top:56px">
    <div class="post-head"><span class="num">04</span><h3 class="post-title">Numquam eius modi tempora dolore magnam aliquam...</h3></div>
    <p class="excerpt" style="margin-top:12px">Numquam eius modi tempora dunt magna aliq uam quaerat voluptatem. Ut enim minima veniam, quis nostrum exercit...</p>
    <p class="posted" style="margin-top:14px">Posted on 23 March,2017</p>
    <div class="meta" style="margin-top:14px"><span>12 Likes</span><span>32 Comments</span><span>Share</span></div>
  </div>
</article>

<article class="card" style="left:130px;top:1836px;width:323px;height:443px">
  <div class="photo" style="left:44px;top:48px;width:237px;height:170px"><span class="pin"></span><div class="fill" role="img" aria-label="Pink gingham album tied with ribbon" style="background:linear-gradient(135deg,#e6a3c7,#f4d9c2)"></div></div>
  <div class="body-sm" style="top:262px">
    <div class="post-head"><span class="num">05</span><h3 class="post-title">Numquam eius modi tempora</h3></div>
    <p class="excerpt" style="margin-top:8px">Numquam eius modi tempora dunt magna aliq uam veniam, quis nostrum exercit...</p>
    <p class="posted" style="margin-top:12px">Posted on 23 March,2017</p>
    <div class="meta" style="margin-top:14px"><span>12 Likes</span><span>32 Comments</span><span>Share</span></div>
  </div>
</article>

<article class="card" style="left:472px;top:1836px;width:324px;height:443px">
  <div class="photo" style="left:44px;top:48px;width:237px;height:170px"><span class="pin"></span><div class="fill" role="img" aria-label="Pink notebook decorated with paper flowers" style="background:linear-gradient(135deg,#ee5a9b,#f7c7db)"></div></div>
  <div class="body-sm" style="top:262px">
    <div class="post-head"><span class="num">06</span><h3 class="post-title">Numquam eius modi tempora</h3></div>
    <p class="excerpt" style="margin-top:8px">Numquam eius modi tempora dunt magna aliq uam veniam, quis nostrum exercit...</p>
    <p class="posted" style="margin-top:12px">Posted on 23 March,2017</p>
    <div class="meta" style="margin-top:14px"><span>12 Likes</span><span>32 Comments</span><span>Share</span></div>
  </div>
</article>

<h2 class="sec-title side-title" style="left:819px;top:656px">Popular Post</h2>
<aside class="side-box" style="top:700px;height:398px">
  <div class="pop"><div class="th" role="img" aria-label="Craft desk thumbnail" style="background:linear-gradient(135deg,#c9bfd6,#eee)"></div><p>Numquam eius tempor incidunt ut labore...<br><span class="date">March 12 , 2017</span></p></div>
  <div class="pop"><div class="th" role="img" aria-label="Blue card thumbnail" style="background:linear-gradient(135deg,#8fc9d6,#e0f0f2)"></div><p>Numquam eius tempor incidunt ut labore...<br><span class="date">March 12 , 2017</span></p></div>
  <div class="pop"><div class="th" role="img" aria-label="Wooden tags thumbnail" style="background:linear-gradient(135deg,#7b5a44,#c7a88c)"></div><p>Numquam eius tempor incidunt ut labore...<br><span class="date">March 12 , 2017</span></p></div>
  <div class="pop" style="border:0"><div class="th" role="img" aria-label="Purple album thumbnail" style="background:linear-gradient(135deg,#5c2e52,#c98ab8)"></div><p>Numquam eius tempor incidunt ut labore...<br><span class="date">March 12 , 2017</span></p></div>
</aside>

<h2 class="sec-title side-title" style="left:819px;top:1120px">Categories</h2>
<aside class="side-box" style="top:1164px;height:428px;padding:8px 0">
  <div class="cat"><i class="ic"></i>Cott is a long established<span class="count">..........( 4 )</span></div>
  <div class="cat"><i class="ic"></i>It is a long established<span class="count">..........( 5 )</span></div>
  <div class="cat"><i class="ic"></i>Lorem Ipsum Dummy<span class="count">..........( 30 )</span></div>
  <div class="cat"><i class="ic"></i>It is a long established<span class="count">..........( 41 )</span></div>
  <div class="cat"><i class="ic"></i>Lorem Ipsum Dummy<span class="count">..........( 7 )</span></div>
  <div class="cat"><i class="ic"></i>It is a long established<span class="count">..........( 23 )</span></div>
  <div class="cat"><i class="ic"></i>Cott is a long established<span class="count">..........( 4 )</span></div>
  <div class="cat"><i class="ic"></i>It is a long established<span class="count">..........( 5 )</span></div>
  <div class="cat"><i class="ic"></i>Lorem Ipsum Dummy<span class="count">..........( 30 )</span></div>
  <div class="cat" style="border:0"><i class="ic"></i>It is a long established<span class="count">..........( 41 )</span></div>
</aside>

<h2 class="sec-title side-title" style="left:819px;top:1616px">Latest Tweets</h2>
<aside class="side-box" style="top:1660px;height:619px">
  <div class="tweet"><i class="av"></i><div class="row"><i class="bird"></i><p><b>@Crafthouse</b> It is a long establish when looking at its layout/http<br><span class="ago">2 Minute ago</span></p></div></div>
  <div class="tweet"><i class="av"></i><div class="row"><i class="bird"></i><p><b>@Crafthouse</b> It is a long establish when looking at its layout/http<br><span class="ago">2 Minute ago</span></p></div></div>
  <div class="tweet"><i class="av"></i><div class="row"><i class="bird"></i><p><b>@Crafthouse</b> It is a long establish when looking at its layout/http<br><span class="ago">2 Minute ago</span></p></div></div>
  <div class="tweet" style="border:0"><i class="av"></i><div class="row"><i class="bird"></i><p><b>@Crafthouse</b> It is a long establish when looking at its layout/http<br><span class="ago">2 Minute ago</span></p></div></div>
</aside>

<section class="band">
  <article class="mini" style="left:132px"><div class="photo"><div class="fill" role="img" aria-label="Pastel greeting card" style="background:linear-gradient(135deg,#9fd1d9,#f2e3d2)"></div></div>
    <div class="body"><div class="post-head"><span class="num">07</span><h3 class="post-title">Numquam eius modi tempora</h3></div><p class="excerpt" style="margin-top:6px">Numquam eius modi tempora dunt quis nostrum exercit...</p><p class="posted" style="margin-top:10px">Posted on 23 March,2017</p><div class="meta" style="margin-top:14px"><span>12</span><span>32</span><span>Share</span></div></div></article>
  <article class="mini" style="left:370px"><div class="photo"><div class="fill" role="img" aria-label="Teal card with red hearts" style="background:linear-gradient(135deg,#4fa6b4,#d76b6b)"></div></div>
    <div class="body"><div class="post-head"><span class="num">08</span><h3 class="post-title">Numquam eius modi tempora</h3></div><p class="excerpt" style="margin-top:6px">Numquam eius modi tempora dunt quis nostrum exercit...</p><p class="posted" style="margin-top:10px">Posted on 23 March,2017</p><div class="meta" style="margin-top:14px"><span>12</span><span>32</span><span>Share</span></div></div></article>
  <article class="mini" style="left:609px"><div class="photo"><div class="fill" role="img" aria-label="Paper houses collage" style="background:linear-gradient(135deg,#6e8b5a,#e2c27a)"></div></div>
    <div class="body"><div class="post-head"><span class="num">09</span><h3 class="post-title">Numquam eius modi tempora</h3></div><p class="excerpt" style="margin-top:6px">Numquam eius modi tempora dunt quis nostrum exercit...</p><p class="posted" style="margin-top:10px">Posted on 23 March,2017</p><div class="meta" style="margin-top:14px"><span>12</span><span>32</span><span>Share</span></div></div></article>
  <article class="mini" style="left:845px"><div class="photo"><div class="fill" role="img" aria-label="Vintage journal with scissors" style="background:linear-gradient(135deg,#8a6a52,#e3d3bd)"></div></div>
    <div class="body"><div class="post-head"><span class="num">10</span><h3 class="post-title">Numquam eius modi tempora</h3></div><p class="excerpt" style="margin-top:6px">Numquam eius modi tempora dunt quis nostrum exercit...</p><p class="posted" style="margin-top:10px">Posted on 23 March,2017</p><div class="meta" style="margin-top:14px"><span>12</span><span>32</span><span>Share</span></div></div></article>
</section>

<section class="news">
  <svg class="env" width="100" height="66" viewBox="0 0 100 66"><rect x="4" y="14" width="92" height="50" fill="none" stroke="rgba(255,255,255,.25)" stroke-width="3"/><polyline points="4,14 50,44 96,14" fill="none" stroke="rgba(255,255,255,.25)" stroke-width="3"/></svg>
  <h3>Subscribe Newsletter :</h3>
  <div class="field">Enter Your Email Id...</div>
  <a class="go">SUBSCRIBE</a>
</section>

<footer class="footer">
  <div class="brand">Crafthouse Studio</div>
  <p class="about">It is a long established fact that a reader will page when looking at its layout....<br><a>Read More</a></p>
  <div class="fcol" style="left:458px"><h4>Quick Links</h4><ul><li>HOME</li><li>ABOUT US</li><li>SERVICES</li><li>PRODUCTS</li><li>COURSES</li><li>BLOG</li><li>CONTACT US</li></ul></div>
  <div class="fcol" style="left:651px"><h4>Information</h4><ul><li>TERMS &amp; CONDITIONS</li><li>PRIVACY POLICY</li><li>DISCLAIMER</li><li>SITE MAP</li><li>MORE INFORMATION</li></ul></div>
  <div class="fcol contact" style="left:898px"><h4>Contact Us</h4><ul><li>(000)-121-1231 (Phone)</li><li>(000)-121-1231 (Fax)</li><li>info@crafthousestudio.com</li><li style="line-height:18px">#lorem Ipsum Dummy text<br>Lorem Ipsum</li></ul></div>
</footer>
<div class="copy">© Copy Right2017 Crafthouse Studio . All rights reserved.<span class="ver">C11</span></div>

</body>
</html>
```